BrightNest

Need a 6 page template designed in Layered PSD for a house cleaning company.

Target Market(s)

People who are selling their homes and need house cleaning

Industry/Entity Type

House cleaning

Number of Pages Required

5+ page

Font styles to use
Sans Serif

Requirements
Must have
• Please see the zip file included with the brief. It has a document with detailed instructions.

```html
<!DOCTYPE html>
<html lang="en">
<head>
<meta charset="utf-8">
<title>BrightNest – Cleaning Services in Barrie Area</title>
<link href="https://fonts.googleapis.com/css2?family=Lato:wght@400;700;900&family=Montserrat:wght@400;500;600;700;800&display=swap" rel="stylesheet">
<style>
:root{
  --navy:#203f8c;
  --navy-deep:#1b3a82;
  --green:#75bd43;
  --green-dark:#5ea332;
  --text:#333a45;
  --muted:#5b6270;
  --white:#ffffff;
  --light:#f4f6fa;
}
*{box-sizing:border-box;margin:0;padding:0}
html,body{width:1200px;height:5240px;overflow:hidden}
body{font-family:"Montserrat",sans-serif;color:var(--text);background:var(--white);position:relative}
.abs{position:absolute}
.btn{display:inline-flex;align-items:center;justify-content:center;border-radius:22px;font-family:"Montserrat",sans-serif;font-weight:600;text-transform:uppercase;letter-spacing:.5px;text-decoration:none}
.btn-green{background:var(--green);color:var(--white)}
.btn-navy{background:var(--navy);color:var(--white)}
.heading{font-family:"Lato",sans-serif;font-weight:700;color:var(--navy);text-transform:uppercase;text-align:center;letter-spacing:.5px}
.photo{position:absolute}

/* header */
.site-header{position:absolute;left:0;top:0;width:1200px;height:98px;background:var(--white)}
.brand{position:absolute;left:62px;top:30px;display:flex;align-items:center;gap:10px}
.brand-dot{width:16px;height:16px;border-radius:50%;background:var(--green)}
.brand-name{font-family:"Montserrat",sans-serif;font-weight:700;font-size:30px;color:var(--navy)}
.main-nav{position:absolute;left:300px;top:38px;display:flex;gap:28px;font-size:14px;color:var(--text)}
.main-nav .active{color:var(--green)}
.header-book{position:absolute;left:750px;top:25px;width:202px;height:46px;font-size:13px}
.header-call{position:absolute;left:962px;top:25px;width:180px;height:46px;border-radius:23px;background:var(--green);color:var(--white);display:flex;align-items:center;gap:10px;padding-left:16px}
.header-call small{display:block;font-size:9px;font-weight:600}
.header-call strong{display:block;font-size:15px;font-weight:600}

/* hero */
.hero{position:absolute;left:0;top:98px;width:1200px;height:614px;background:linear-gradient(90deg,#2a4c9c 0%,#3b62b4 55%,#2f56a8 100%)}
.hero-title{position:absolute;left:58px;top:138px;font-weight:700;font-size:49px;line-height:57px;color:var(--white);text-transform:uppercase}
.hero-title span{color:var(--green)}
.hero-text{position:absolute;left:60px;top:318px;width:440px;font-size:15px;line-height:25px;color:var(--white)}
.hero-cta{position:absolute;left:60px;top:436px;width:282px;height:42px;font-size:14px}
.hero-photo{left:600px;top:50px;width:440px;height:564px;background:linear-gradient(180deg,#5577c0 0%,#3e7f3a 60%,#c8252a 100%);border-radius:4px}
.sparkle{position:absolute;border:3px solid var(--white);border-radius:50%}

/* intro */
.intro-title{position:absolute;left:0;top:782px;width:1200px;font-size:29px;line-height:42px}
.intro-photo{left:250px;top:940px;width:306px;height:375px;background:linear-gradient(180deg,#f2f2f2 0%,#6cb23f 55%,#c52a2e 100%)}
.intro-text{position:absolute;left:624px;top:966px;width:420px;font-size:12.5px;line-height:23px;color:var(--muted)}
.intro-text p{margin-bottom:14px}

/* cta pill */
.cta-pill{position:absolute;left:138px;top:1318px;width:938px;height:162px;background:var(--green);border-radius:81px}
.cta-pill h3{position:absolute;left:54px;top:42px;font-family:"Lato",sans-serif;font-weight:700;font-size:23px;color:var(--navy);text-transform:uppercase;letter-spacing:.5px}
.cta-pill p{position:absolute;left:58px;top:82px;width:560px;font-size:13px;line-height:25px;color:var(--white)}
.cta-circle{position:absolute;right:8px;top:8px;width:146px;height:146px;border-radius:50%;background:var(--navy);color:var(--white);display:flex;align-items:center;justify-content:center;text-align:center;font-size:14px;font-weight:600;text-transform:uppercase;line-height:20px}

/* services */
.services-title{position:absolute;left:0;top:1552px;width:1200px;font-size:28px}
.services{position:absolute;left:0;top:1640px;width:1200px;height:510px;display:flex}
.service-card{width:300px;height:510px;position:relative;text-align:center;color:var(--white)}
.service-card.navy{background:var(--navy)}
.service-card.green{background:var(--green)}
.service-photo{position:absolute;left:0;top:0;width:100%;height:240px}
.service-card h4{position:absolute;left:0;top:278px;width:100%;font-family:"Lato",sans-serif;font-weight:700;font-size:19px;text-transform:uppercase;letter-spacing:.5px}
.service-card p{position:absolute;left:22px;top:320px;width:256px;font-size:13.5px;line-height:23px}
.service-card .btn{position:absolute;left:75px;top:434px;width:150px;height:42px;font-size:14px}

/* included */
.included-title{position:absolute;left:0;top:2218px;width:1200px;font-size:29px;line-height:42px}
.checklist{position:absolute;top:2345px;width:260px}
.checklist h5{font-family:"Lato",sans-serif;font-weight:700;font-size:21px;color:var(--green);margin-bottom:14px}
.checklist ul{list-style:none;font-size:13.5px;color:var(--text)}
.checklist li{height:30px;padding-left:16px;position:relative}
.checklist li::before{content:"";position:absolute;left:2px;top:8px;width:4px;height:4px;border-radius:50%;background:var(--text)}

/* band */
.band{position:absolute;left:0;top:2616px;width:1200px;height:494px}
.band-title{position:absolute;left:0;top:2716px;width:1200px;font-size:29px;line-height:42px;color:var(--white)}
.band-text{position:absolute;left:255px;top:2862px;width:690px;font-size:13.5px;line-height:22px;color:var(--white);text-align:center}
.band-text p{margin-bottom:14px}
.band-cta{position:absolute;left:466px;top:2988px;width:282px;height:42px;font-size:14px}

/* blog */
.blog-title{position:absolute;left:0;top:3184px;width:1200px;font-size:29px}
.blog-card{position:absolute;top:3268px;width:345px}
.blog-photo{position:relative;width:345px;height:228px}
.blog-card h6{font-family:"Lato",sans-serif;font-weight:700;font-size:15.5px;line-height:24px;color:var(--text);margin:20px 2px 12px}
.blog-card p{font-size:12px;line-height:22px;color:var(--muted);padding:0 2px}

/* areas */
.areas{position:absolute;left:0;top:3745px;width:1200px;height:565px;background:var(--green)}
.areas-title{position:absolute;left:0;top:3812px;width:1200px;font-size:29px}
.area-col{position:absolute;top:3880px;list-style:none;font-size:14.5px;color:var(--white)}
.area-col li{height:36px;padding:6px 16px 0 28px;position:relative}
.area-col li::before{content:"";position:absolute;left:12px;top:14px;width:5px;height:5px;border-radius:50%;background:var(--white)}
.area-col li.current{background:var(--navy);border-radius:16px;height:30px;padding-top:5px}
.area-col li.note{color:var(--navy);line-height:26px;height:auto;padding-top:0}
.map{left:156px;top:4050px;width:888px;height:450px;background:linear-gradient(135deg,#dfe8d9 0%,#cfe0c6 45%,#8fb4e8 60%,#7ea9e6 100%)}

/* availability */
.avail-title{position:absolute;left:138px;top:4610px;font-family:"Lato",sans-serif;font-weight:700;font-size:33px;color:var(--navy);text-transform:uppercase;letter-spacing:1px}
.avail-list{position:absolute;left:140px;top:4672px;list-style:none;color:var(--text)}
.avail-list li{display:flex;align-items:center;gap:14px;margin-bottom:12px}
.avail-list .big{font-size:21px}
.avail-list .mid{font-size:16.5px}
.avail-list span.hl{color:var(--green)}
.avail-list .indent{padding-left:40px}
.avail-cta{position:absolute;left:140px;top:4836px;width:284px;height:44px;font-size:14px}
.avail-photo{left:710px;top:4545px;width:285px;height:435px;background:linear-gradient(180deg,#f5f5f5 0%,#6db33f 50%,#c52a2e 100%)}

/* footer */
.site-footer{position:absolute;left:0;top:4980px;width:1200px;height:260px;background:var(--navy);color:var(--white)}
.footer-brand{position:absolute;left:62px;top:92px;display:flex;align-items:center;gap:12px}
.footer-brand .brand-name{color:var(--white);font-size:38px}
.footer-text{position:absolute;left:426px;top:22px;width:330px;font-size:13px;line-height:27px}
.footer-text a{color:var(--green);text-decoration:none}
.footer-contact{position:absolute;left:855px;top:30px;font-size:15px}
.footer-contact .phone{color:var(--green);font-size:19px;margin-bottom:14px}
.footer-contact a{display:block;color:var(--white);text-decoration:underline;margin:0 0 20px 8px;font-size:14.5px}
.copyright{position:absolute;left:0;top:228px;width:1200px;text-align:center;font-size:11px}
.copyright span{color:var(--green)}
</style>
</head>
<body>

<header class="site-header">
  <div class="brand"><span class="brand-dot"></span><span class="brand-name">BrightNest</span></div>
  <nav class="main-nav">
    <span class="active">+ Home</span><span>Services</span><span>What's Included</span><span>For Realtors</span><span>Blog</span>
  </nav>
  <a class="btn btn-navy header-book">Book a Appointment</a>
  <div class="header-call">
    <svg width="24" height="24" viewBox="0 0 24 24"><path fill="#fff" d="M6.6 10.8a15 15 0 0 0 6.6 6.6l2.2-2.2a1 1 0 0 1 1-.25 11.4 11.4 0 0 0 3.6.57 1 1 0 0 1 1 1V20a1 1 0 0 1-1 1A17 17 0 0 1 3 4a1 1 0 0 1 1-1h3.5a1 1 0 0 1 1 1c0 1.25.2 2.45.57 3.57a1 1 0 0 1-.25 1z"/></svg>
    <div><small>GIVE US A CALL:</small><strong>+1 555 014 2290</strong></div>
  </div>
</header>

<section class="hero">
  <h1 class="hero-title">Find Cleaning<br>Services in<br><span>Barrie Area</span></h1>
  <p class="hero-text">Whether you're moving into or out of a Barrie area home, apartment, or rental property, our Barrie area Pre-Sale, Move-In, and Move-Out Deep Cleaning Services are the perfect solution for you.</p>
  <a class="btn btn-green hero-cta">Schedule an Appointment</a>
  <div class="photo hero-photo" role="img" aria-label="Smiling cleaner in apron and red gloves holding a bucket of cleaning supplies, giving a thumbs up"></div>
  <span class="sparkle" style="left:648px;top:200px;width:26px;height:26px"></span>
  <span class="sparkle" style="left:706px;top:220px;width:20px;height:20px"></span>
  <span class="sparkle" style="left:638px;top:250px;width:18px;height:18px"></span>
</section>

<h2 class="heading intro-title">The only Barrie area cleaning service that<br>specializes in deep pre-sale, move-in, &amp;<br>move-out house cleanings</h2>
<div class="photo intro-photo" role="img" aria-label="Cleaner holding a cloth and a blue plate, wearing red gloves"></div>
<div class="intro-text">
  <p>Welcome to the only Barrie area cleaning service specializing in deep move-in, move-out, and pre-sale house cleanings.</p>
  <p>Moving in or out of a home can be daunting with so much to organize and prepare. Cleaning is often the last thing on your mind, but it's essential to sell your home quickly and to have a clean, hygienic environment in your new home for you and your family when you move in.</p>
  <p>Whether you're moving in or out of a Barrie area home, apartment, or rental property, our Barrie area Pre-Sale, Move-In, and Move-Out Deep Cleaning Services are the perfect solution for you.</p>
</div>

<div class="cta-pill">
  <h3>Contact us today to schedule an appointment</h3>
  <p>Let us take the hassle out of your client's move and ensure their Barrie home is deep-cleaned, fresh, and ready.</p>
  <div class="cta-circle">Schedule an<br>Appointment</div>
</div>

<h2 class="heading services-title">Cleaning Services We Offer</h2>
<section class="services">
  <article class="service-card navy">
    <div class="service-photo" role="img" aria-label="Couple with laundry and a sale sign" style="background:linear-gradient(180deg,#f4f4f4,#d8403a)"></div>
    <h4>Pre-Sale Cleanings</h4>
    <p>Are You Putting Your Barrie Area Home Up For Sale?</p>
    <a class="btn btn-green">Know More</a>
  </article>
  <article class="service-card green">
    <div class="service-photo" role="img" aria-label="Team cleaning a bright room" style="background:linear-gradient(180deg,#e8efe6,#8fb77a)"></div>
    <h4>Move-In Cleanings</h4>
    <p>Take the Stress Out of Your Move &amp; Have Your Home Sparkling Clean Before You Move In</p>
    <a class="btn btn-navy">Know More</a>
  </article>
  <article class="service-card navy">
    <div class="service-photo" role="img" aria-label="Woman among moving boxes and a sofa" style="background:linear-gradient(180deg,#f3f3f3,#c9a27a)"></div>
    <h4>Move-Out Cleanings</h4>
    <p>Cleaned &amp; Ready for The Next Occupants</p>
    <a class="btn btn-green">Know More</a>
  </article>
  <article class="service-card green">
    <div class="service-photo" role="img" aria-label="Old household items and junk on a shelf" style="background:linear-gradient(180deg,#ece8e2,#8a5a3a)"></div>
    <h4>Junk Removal</h4>
    <p>Your Barrie Area Home Up For Junk Removal?</p>
    <a class="btn btn-navy">Know More</a>
  </article>
</section>

<h2 class="heading included-title">Included with your pre-sale, move-in or<br>move-out deep house cleaning service</h2>
<div class="checklist" style="left:70px"><h5>Kitchen Cleaning</h5><ul><li>Countertops</li><li>Stove</li><li>Refrigerator</li><li>Cabinets</li><li>Sink</li><li>Windows</li></ul></div>
<div class="checklist" style="left:348px"><h5>Bathroom Cleaning</h5><ul><li>Toilet</li><li>Sink</li><li>Shower and Bathtub</li><li>Mirrors</li><li>Windows</li></ul></div>
<div class="checklist" style="left:625px"><h5>Bedrooms Cleaning</h5><ul><li>Bed</li><li>Furniture</li><li>Mirrors</li><li>Windows</li><li>Closet</li></ul></div>
<div class="checklist" style="left:905px"><h5>Living Areas Cleaning</h5><ul><li>Furniture</li><li>Floors.</li><li>Windows</li><li>Electronics</li><li>Carpets</li></ul></div>

<svg class="band" viewBox="0 0 1200 494" aria-hidden="true"><polygon points="0,48 600,0 1200,48 1200,494 0,494" fill="#203f8c"/></svg>
<h2 class="heading band-title">The only Barrie area cleaning service that<br>specializes in deep pre-sale, move-in &amp;<br>move-out house cleanings</h2>
<div class="band-text">
  <p>Whether you're moving into or out of a Barrie area home, apartment, or rental property, our Barrie area Pre-Sale, Move-In, and Move-Out Deep Cleaning Services are the perfect solution for you.</p>
  <p>Contact Us Today To Schedule An Appointment, and let us take care of the daunting task of having your home deep cleaned so that you can enjoy your new Barrie area home from day one.</p>
</div>
<a class="btn btn-green band-cta">Schedule an Appointment</a>

<h2 class="heading blog-title">Latest Blog</h2>
<article class="blog-card" style="left:60px">
  <div class="blog-photo" role="img" aria-label="Tired couple resting among moving boxes" style="background:linear-gradient(180deg,#eee9e2,#b99872)"></div>
  <h6>Lorem Ipsum has been the industry's stand the dummy text ever since the.</h6>
  <p>Lorem Ipsum has been the industry's standard dummy text ever since the 1500s, when an unknown printer took a galley of type and scrambled it to make.</p>
</article>
<article class="blog-card" style="left:428px">
  <div class="blog-photo" role="img" aria-label="Woman with cleaning supplies on a yellow sofa" style="background:linear-gradient(180deg,#f2f2f0,#e8d84a)"></div>
  <h6>Lorem Ipsum has been the industry's stand the dummy text ever since the.</h6>
  <p>Lorem Ipsum has been the industry's standard dummy text ever since the 1500s, when an unknown printer took a galley of type and scrambled it to make.</p>
</article>
<article class="blog-card" style="left:795px">
  <div class="blog-photo" role="img" aria-label="Couple packing boxes in a new home" style="background:linear-gradient(180deg,#5d6a66,#a07a5c)"></div>
  <h6>Lorem Ipsum has been the industry's stand the dummy text ever since the.</h6>
  <p>Lorem Ipsum has been the industry's standard dummy text ever since the 1500s, when an unknown printer took a galley of type and scrambled it to make.</p>
</article>

<section class="areas"></section>
<h2 class="heading areas-title">Areas We Service</h2>
<ul class="area-col" style="left:148px"><li class="current">Barrie</li><li>Innisfil</li><li>Springwater</li><li>Minesing</li></ul>
<ul class="area-col" style="left:318px"><li>Orillia</li><li>Wasaga</li><li>Midland</li><li>Angus</li></ul>
<ul class="area-col" style="left:468px"><li>Collingwood</li><li>New Lowell</li><li>Oro-Medonte</li><li>Shanty Bay</li></ul>
<ul class="area-col" style="left:662px"><li>Horseshoe Valley</li><li>Coldwater</li><li>Stayner</li><li>Creemore</li></ul>
<ul class="area-col" style="left:872px"><li>Alliston</li><li class="note">And everywhere<br>in between</li></ul>
<div class="photo map" role="img" aria-label="Map of the Barrie area and Lake Simcoe showing service locations"></div>

<h2 class="avail-title">Availability</h2>
<ul class="avail-list">
  <li class="big"><svg width="22" height="22" viewBox="0 0 24 24" fill="none" stroke="#75bd43" stroke-width="1.8"><rect x="3" y="5" width="18" height="16" rx="2"/><path d="M3 10h18M8 3v4M16 3v4"/></svg>Open 7 Days a Week <span class="hl">(Monday-Sunday)</span></li>
  <li class="mid"><svg width="22" height="22" viewBox="0 0 24 24" fill="none" stroke="#75bd43" stroke-width="1.8"><circle cx="12" cy="12" r="9"/><path d="M12 7v5l3 2"/></svg>Hours 8:00 am – 9:00 pm</li>
  <li class="mid indent">Evenings &amp; Weekends&nbsp;<span class="hl">(Yes)</span></li>
  <li class="mid indent">Short Notice&nbsp;<span class="hl">(Yes)</span></li>
</ul>
<a class="btn btn-green avail-cta">Schedule an Appointment</a>
<div class="photo avail-photo" role="img" aria-label="Cleaner in green shirt and apron holding red gloves"></div>
<span class="sparkle" style="left:940px;top:4628px;width:20px;height:20px;border-color:#75bd43"></span>
<span class="sparkle" style="left:988px;top:4600px;width:28px;height:28px;border-color:#75bd43"></span>
<span class="sparkle" style="left:1008px;top:4662px;width:20px;height:20px;border-color:#75bd43"></span>

<footer class="site-footer">
  <div class="footer-brand"><span class="brand-dot"></span><span class="brand-name">BrightNest</span></div>
  <p class="footer-text"><a>Contact Us Today To Schedule An Appointment,</a> and let us take care of the daunting task of having your home deep cleaned so that you can enjoy your new Barrie area home from day one.</p>
  <div class="footer-contact">
    <div class="phone">+1 555 014 2290</div>
    <a>Services Area</a>
    <a>Contact US</a>
  </div>
  <p class="copyright">©<span>BrightNest</span> - 2023 All rights reserved.</p>
</footer>

</body>
</html>
```